Human Resource Consulting practice needs a business card design

We need a business card design (double sided colour) for our Human Resource (HR) consulting practice in regional New South Wales, australia. Our business name is Staffwise Partners. We support small and medium business across the Mid North Coast of New South Wales by providing them with outsourced HR support, services and products to help them achieve compliance with workplace legislation and across all areas of the employment lifecycle from recruitment to termination and everything in between. Our corporate colours are hot pink and black. The final design should communicate professionalism, trust, people focus.
I have attached the current (old) business card for your reference.

Target Market(s)

Business owners and high level managers

Industry/Entity Type

Business

Contact Information for Business Card

Name
Title
Phone no
Mobile no
Address
PO Box
email address
website

Colors
e34197

Requirements
Must have
• Tempate for changing business card personal details including Name, position title, mobile number, email address.
• Keep current logo and colours as per attached
• Logo must be presented in 2 colours or black only not white
Nice to have
• One side logo and graphic only other side logo and personal details
Should not have
• Should not be the same as the current version (attached) but a modern interpretation.
• Does not need a busy reverse side with our list of services as per current version. I feel this is too busy.
• No photos

```html
<!DOCTYPE html>
<html lang="en">
<head>
<meta charset="utf-8">
<title>Staffwise Partners – Business Card</title>
<link rel="stylesheet" href="https://fonts.googleapis.com/css2?family=Michroma&display=swap">
<style>
  :root {
    --hot-pink: #e0137f;
    --ink: #1a1a1a;
    --card: #ececec;
    --card-band: #c9c9c9;
    --backdrop: #2a2a2a;
  }
  * { margin: 0; padding: 0; box-sizing: border-box; }
  html, body { width: 1200px; height: 900px; overflow: hidden; }
  body {
    background: var(--backdrop);
    font-family: "Michroma", sans-serif;
    color: var(--ink);
    display: flex;
    flex-direction: column;
    align-items: center;
    justify-content: center;
    gap: 56px;
  }
  .card {
    position: relative;
    width: 580px;
    height: 354px;
    background: var(--card);
    border-radius: 22px;
    overflow: hidden;
  }
  .card-graphics { position: absolute; inset: 0; width: 100%; height: 100%; }
  .brand-name {
    display: flex;
    align-items: center;
    gap: 10px;
    color: var(--hot-pink);
    font-size: 26px;
    letter-spacing: 0.5px;
    line-height: 1.15;
  }
  .brand-mark {
    width: 10px;
    height: 10px;
    background: var(--hot-pink);
    flex: none;
  }
  .front .brand-name { position: absolute; left: 40px; top: 40px; width: 300px; }
  .contact-list {
    position: absolute;
    left: 40px;
    top: 150px;
    list-style: none;
    font-size: 11px;
    line-height: 20px;
  }
  .contact-list li { display: flex; align-items: center; gap: 8px; }
  .contact-list .address { padding-left: 22px; margin-bottom: 6px; }
  .contact-icon { width: 14px; height: 14px; flex: none; }
  .person {
    position: absolute;
    right: 40px;
    top: 170px;
    text-align: right;
  }
  .person-name { color: var(--hot-pink); font-size: 20px; font-weight: 400; }
  .person-title { font-size: 10px; margin-top: 6px; letter-spacing: 0.5px; }
  .back { display: flex; flex-direction: column; align-items: center; justify-content: center; gap: 18px; }
  .back .brand-name { font-size: 32px; }
  .back-web { font-size: 13px; letter-spacing: 0.5px; }
</style>
</head>
<body>

<section class="card front" aria-label="Business card front">
  <svg class="card-graphics" viewBox="0 0 580 354" aria-hidden="true">
    <polygon points="0,264 300,354 0,354" fill="var(--card-band)"/>
    <polygon points="0,248 0,262 240,354 280,354" fill="var(--hot-pink)"/>
  </svg>
  <div class="brand-name"><span class="brand-mark"></span>Staffwise Partners</div>
  <ul class="contact-list">
    <li class="address">PO Box 218, Karrawong<br>NSW 2440</li>
    <li>
      <svg class="contact-icon" viewBox="0 0 14 14"><path d="M3 1l3 3-1.5 1.5a8 8 0 0 0 4 4L10 8l3 3-2 2C6 13 1 8 1 3z" fill="var(--hot-pink)"/></svg>
      0400 555 218
    </li>
    <li>
      <svg class="contact-icon" viewBox="0 0 14 14"><rect x="1" y="3" width="12" height="8" fill="var(--hot-pink)"/><path d="M1 3l6 5 6-5" fill="none" stroke="var(--card)" stroke-width="1.2"/></svg>
      claire@staffwisepartners.com.au
    </li>
    <li>
      <svg class="contact-icon" viewBox="0 0 14 14" fill="none" stroke="var(--hot-pink)" stroke-width="1.1"><circle cx="7" cy="7" r="5.5"/><ellipse cx="7" cy="7" rx="2.5" ry="5.5"/><path d="M1.5 7h11M2.5 4.2h9M2.5 9.8h9"/></svg>
      www.staffwisepartners.com.au
    </li>
  </ul>
  <div class="person">
    <h1 class="person-name">Claire Benton</h1>
    <p class="person-title">PRINCIPAL CONSULTANT</p>
  </div>
</section>

<section class="card back" aria-label="Business card back">
  <div class="brand-name"><span class="brand-mark"></span>Staffwise Partners</div>
  <p class="back-web">www.staffwisepartners.com.au</p>
</section>

</body>
</html>
```